Need updated stationery design for chiropractic clinic

We recently moved our office and are looking to refresh our letterhead, business cards, presentation folder and envelopes. I tend to prefer simple, clean designs. We communicate with a lot of attorneys and want to exude professionalism. I have attached our logo and 2 additional versions (all white and white letters instead of grey).

Target Market(s)

Other medical professionals and attorneys. Business cards will go to patients as well.

Industry/Entity Type

Healthcare

```html
<!DOCTYPE html>
<html lang="en">
<head>
<meta charset="utf-8">
<title>SpineWell Injury Care Clinic – Stationery</title>
<link rel="stylesheet" href="https://fonts.googleapis.com/css2?family=Open+Sans:wght@400;600&family=Raleway:wght@700&family=Roboto+Condensed:wght@300;400&display=swap">
<style>
  :root {
    --brand-blue: #2a93c1;
    --brand-teal: #3fb8c4;
    --paper: #f7f7f7;
    --backdrop: #e9e9e9;
    --ink: #4a4a4a;
    --ink-soft: #6b6b6b;
    --white: #ffffff;
  }
  * { margin: 0; padding: 0; box-sizing: border-box; }
  html, body { width: 1200px; height: 795px; overflow: hidden; }
  body {
    position: relative;
    background: var(--backdrop);
    font-family: "Open Sans", sans-serif;
    color: var(--ink);
  }
  .sheet { position: absolute; background: var(--paper); box-shadow: 0 2px 6px rgba(0,0,0,.12); overflow: hidden; }

  .brand { display: flex; align-items: center; gap: 4px; }
  .brand-mark { background: var(--brand-blue); flex: none; }
  .brand-name { font-family: "Raleway", sans-serif; font-weight: 700; color: var(--brand-blue); line-height: 1; }
  .brand-tag { font-family: "Roboto Condensed", sans-serif; font-weight: 300; color: var(--ink); line-height: 1.1; letter-spacing: .02em; }

  .footer-band { position: absolute; left: 0; bottom: 0; width: 100%; }
  .footer-url { position: absolute; right: 0; bottom: 0; color: var(--white); font-family: "Roboto Condensed", sans-serif; text-align: center; }

  /* Letterhead */
  .letterhead { left: 292px; top: 99px; width: 293px; height: 415px; }
  .letterhead .brand { position: absolute; left: 32px; top: 28px; }
  .letterhead .brand-mark { width: 24px; height: 24px; }
  .letterhead .brand-name { font-size: 12px; }
  .letterhead .brand-tag { font-size: 6px; }
  .contact { font-family: "Roboto Condensed", sans-serif; font-size: 5.6px; line-height: 7.2px; color: var(--ink-soft); }
  .letterhead .contact { position: absolute; left: 195px; top: 21px; }
  .contact-line { display: flex; align-items: center; gap: 2px; }
  .contact-line svg { width: 5px; height: 5px; fill: var(--brand-blue); }
  .letter-body { position: absolute; left: 32px; top: 106px; width: 231px; font-size: 4.7px; line-height: 7.6px; text-align: justify; color: var(--ink); }
  .letter-body p { margin-bottom: 7.6px; }
  .signature { width: 34px; height: 34px; background: linear-gradient(135deg, #e6e6e6, #d8d8d8); margin-top: 4px; }
  .letterhead .footer-band { height: 12px; }
  .letterhead .footer-url { width: 86px; height: 10px; font-size: 5.6px; line-height: 10px; }

  /* Folder */
  .folder { left: 636px; top: 80px; width: 347px; height: 437px; background: var(--brand-blue); }
  .folder-spine { position: absolute; left: 5px; top: 0; width: 15px; height: 100%;
    border-left: 1px solid rgba(0,0,0,.12); border-right: 1px solid rgba(0,0,0,.12); }
  .folder .brand { position: absolute; right: 24px; bottom: 18px; gap: 6px; }
  .folder .brand-mark { width: 36px; height: 36px; background: var(--white); }
  .folder .brand-name { font-size: 18px; color: var(--white); }
  .folder .brand-tag { font-size: 9.5px; color: var(--white); }

  /* Business cards */
  .card { left: 187px; width: 133px; height: 75px; }
  .card-front { top: 551px; background: var(--brand-blue); display: flex; flex-direction: column; align-items: center; justify-content: center; gap: 5px; }
  .card-front .brand-mark { width: 24px; height: 24px; background: var(--white); }
  .card-front .brand-name { font-size: 12px; color: var(--white); }
  .card-front .brand-tag { font-size: 6.4px; color: var(--white); text-align: center; }
  .card-back { top: 646px; }
  .card-back .brand { position: absolute; left: 11px; top: 30px; gap: 3px; }
  .card-back .brand-mark { width: 13px; height: 13px; }
  .card-back .brand-name { font-size: 7px; }
  .card-back .brand-tag { font-size: 3.2px; }
  .card-divider { position: absolute; left: 67px; top: 17px; width: .5px; height: 42px; background: #bdbdbd; }
  .card-details { position: absolute; left: 74px; top: 18px; }
  .person-name { font-family: "Roboto Condensed", sans-serif; font-weight: 400; font-size: 4.6px; color: var(--brand-blue); text-transform: uppercase; }
  .person-role { font-family: "Roboto Condensed", sans-serif; font-size: 3.6px; color: var(--ink-soft); margin-bottom: 5px; }
  .card-back .contact { font-size: 3.6px; line-height: 5px; }
  .card-back .contact-line svg { width: 3px; height: 3px; }
  .card-back .footer-band { height: 6px; }
  .card-back .footer-url { width: 50px; height: 5px; font-size: 3.4px; line-height: 5px; }

  /* Envelopes */
  .envelope { top: 561px; width: 329px; height: 157px; }
  .envelope-front { left: 353px; }
  .envelope-front .brand { position: absolute; left: 17px; top: 19px; gap: 3px; }
  .envelope-front .brand-mark { width: 21px; height: 21px; }
  .envelope-front .brand-name { font-size: 10.5px; }
  .envelope-front .brand-tag { font-size: 5.2px; }
  .return-address { position: absolute; left: 26px; top: 44px; font-family: "Roboto Condensed", sans-serif; font-size: 5.4px; line-height: 6.6px; color: var(--ink); text-align: center; }
  .envelope-front .footer-band { height: 14px; }
  .envelope-front .footer-url { width: 100px; height: 12px; font-size: 6.6px; line-height: 12px; }
  .envelope-back { left: 713px; }
  .envelope-flap { position: absolute; left: 0; top: 0; width: 100%; height: 56px; }
  .flap-mark { position: absolute; left: 148px; top: 12px; width: 33px; height: 33px; background: var(--white); }
</style>
</head>
<body>

  <section class="sheet letterhead" aria-label="Letterhead">
    <div class="brand">
      <span class="brand-mark"></span>
      <div><div class="brand-name">SpineWell</div><div class="brand-tag">INJURY CARE CLINIC</div></div>
    </div>
    <address class="contact">
      <div>48 Harbourview Lane</div>
      <div>Fredericton, NB E3B2K7</div>
      <div class="contact-line"><svg viewBox="0 0 10 10"><path d="M2 0l2 2.5-1.2 1.2a6 6 0 0 0 3.5 3.5L7.5 6 10 8 8.5 10C4 10 0 6 0 1.5z"/></svg>(555) 318-4920</div>
      <div class="contact-line"><svg viewBox="0 0 10 10"><path d="M2 0h6v3H2zM0 3.5h10v4.5H8V6H2v2H0zM2.5 7h5v3h-5z"/></svg>(555) 318-4921</div>
      <div class="contact-line"><svg viewBox="0 0 10 10"><path d="M0 2h10v6H0zM.8 2.6 5 5.6l4.2-3" fill="none" stroke="#2a93c1" stroke-width="1"/></svg>hello@spinewellclinic.com</div>
    </address>
    <div class="letter-body">
      <p>Dear customer,</p>
      <p>Lorem ipsum dolor sit amet, consectetur adipisicing elit, sed do eiusmod tempor incididunt ut labore et dolore magna aliqua. Ut enim ad minim veniam, quis nostrud exercitation ullamco laboris nisi ut aliquip ex ea commodo consequat. Duis aute irure dolor in reprehenderit in voluptate velit esse cillum dolore eu fugiat nulla pariatur. Excepteur sint occaecat cupidatat non proident, sunt in culpa qui officia deserunt mollit anim id est laborum.</p>
      <p>Lorem ipsum dolor sit amet, consectetur adipisicing elit, sed do eiusmod tempor incididunt ut labore et dolore magna aliqua. Ut enim ad minim veniam, quis nostrud exercitation ullamco laboris nisi ut aliquip ex ea commodo consequat. Duis aute irure dolor in reprehenderit in voluptate velit esse cillum dolore eu fugiat nulla pariatur. Excepteur sint occaecat cupidatat non proident, sunt in culpa qui officia deserunt mollit anim id est laborum.</p>
      <p>Lorem ipsum dolor sit amet, consectetur adipisicing elit, sed do eiusmod tempor incididunt ut labore et dolore magna aliqua. Ut enim ad minim veniam, quis nostrud exercitation ullamco laboris nisi ut aliquip ex ea commodo consequat. Duis aute irure dolor in reprehenderit in voluptate velit esse cillum dolore eu fugiat nulla pariatur. Excepteur sint occaecat cupidatat non proident, sunt in culpa qui officia deserunt mollit anim id est laborum.</p>
      <p>Lorem ipsum dolor sit amet, consectetur adipisicing elit, sed do eiusmod tempor incididunt ut labore et dolore magna aliqua. Ut enim ad minim veniam, quis nostrud exercitation ullamco laboris nisi ut aliquip ex ea commodo consequat. Duis aute irure dolor in reprehenderit.</p>
      <p>Yours Sincerely,</p>
      <div class="signature" role="img" aria-label="Handwritten signature"></div>
    </div>
    <svg class="footer-band" viewBox="0 0 293 12" preserveAspectRatio="none">
      <rect x="0" y="1.5" width="198" height="1.2" fill="var(--brand-teal)"/>
      <rect x="0" y="9" width="293" height="3" fill="var(--brand-blue)"/>
      <path d="M193 12 L203 2 H293 V12 Z" fill="var(--brand-blue)"/>
    </svg>
    <div class="footer-url">www.spinewellclinic.com</div>
  </section>

  <section class="sheet folder" aria-label="Presentation folder">
    <div class="folder-spine"></div>
    <div class="brand">
      <span class="brand-mark"></span>
      <div><div class="brand-name">SpineWell</div><div class="brand-tag">INJURY CARE CLINIC</div></div>
    </div>
  </section>

  <section class="sheet card card-front" aria-label="Business card front">
    <span class="brand-mark"></span>
    <div><div class="brand-name">SpineWell</div><div class="brand-tag">INJURY CARE CLINIC</div></div>
  </section>

  <section class="sheet card card-back" aria-label="Business card back">
    <div class="brand">
      <span class="brand-mark"></span>
      <div><div class="brand-name">SpineWell</div><div class="brand-tag">INJURY CARE CLINIC</div></div>
    </div>
    <div class="card-divider"></div>
    <div class="card-details">
      <div class="person-name">Daniel R. Whitford</div>
      <div class="person-role">Founder &amp; CEO</div>
      <address class="contact">
        <div>48 Harbourview Lane</div>
        <div>Fredericton, NB E3B2K7</div>
        <div class="contact-line"><svg viewBox="0 0 10 10"><path d="M2 0l2 2.5-1.2 1.2a6 6 0 0 0 3.5 3.5L7.5 6 10 8 8.5 10C4 10 0 6 0 1.5z"/></svg>(555) 318-4920</div>
        <div class="contact-line"><svg viewBox="0 0 10 10"><path d="M2 0h6v3H2zM0 3.5h10v4.5H8V6H2v2H0zM2.5 7h5v3h-5z"/></svg>(555) 318-4921</div>
        <div class="contact-line"><svg viewBox="0 0 10 10"><path d="M0 2h10v6H0z"/></svg>hello@spinewellclinic.com</div>
      </address>
    </div>
    <svg class="footer-band" viewBox="0 0 133 6" preserveAspectRatio="none">
      <rect x="0" y="1" width="82" height=".6" fill="var(--brand-teal)"/>
      <rect x="0" y="4.5" width="133" height="1.5" fill="var(--brand-blue)"/>
      <path d="M80 6 L85 1 H133 V6 Z" fill="var(--brand-blue)"/>
    </svg>
    <div class="footer-url">www.spinewellclinic.com</div>
  </section>

  <section class="sheet envelope envelope-front" aria-label="Envelope front">
    <div class="brand">
      <span class="brand-mark"></span>
      <div><div class="brand-name">SpineWell</div><div class="brand-tag">INJURY CARE CLINIC</div></div>
    </div>
    <address class="return-address">
      <div>48 Harbourview Lane</div>
      <div>Fredericton, NB E3B2K7</div>
    </address>
    <svg class="footer-band" viewBox="0 0 329 14" preserveAspectRatio="none">
      <rect x="0" y="2" width="225" height="1.3" fill="var(--brand-teal)"/>
      <rect x="0" y="10.5" width="329" height="3.5" fill="var(--brand-blue)"/>
      <path d="M218 14 L230 2 H329 V14 Z" fill="var(--brand-blue)"/>
    </svg>
    <div class="footer-url">www.spinewellclinic.com</div>
  </section>

  <section class="sheet envelope envelope-back" aria-label="Envelope back">
    <svg class="envelope-flap" viewBox="0 0 329 56" preserveAspectRatio="none">
      <path d="M0 0 H329 L322 47 Q321 55 313 55 H16 Q8 55 7 47 Z" fill="var(--brand-blue)"/>
    </svg>
    <span class="flap-mark"></span>
  </section>

</body>
</html>
```